Entertainment Sound and Lighting company Business card

We need a professional looking business card designed for my growing entertainment sound and lighting company based in Sydney, Australia called "Kestrel Sound"

We provide technical production services (sound systems/lighting/vision) for events ranging from band gigs, weddings, corporate functions etc.

The business card needs to contain the following information:

Bartholomew Quenneville
Audio Engineer
Phone: 0478 615 027
Email: bartholomew@kestrelsound.com.au
Website: www.kestrelsound.com.au

Business logo has been attached in .ai format, please contact me if you need me to provide other files.

Target Market(s)

We need a business card that reflects our modern and professional company but still looks professional to appeal to our corporate clients.
We have a very broad target market spanning from bands needing PA systems for their gigs (18-30yrs) to event companies needing sound and lighting for weddings and other functions.

Industry/Entity Type

Business

Requirements
Must have
• Needs to include the logo that is attached of course, and the colour scheme.
Nice to have
• - Double sided

```html
<!DOCTYPE html>
<html lang="en">
<head>
<meta charset="utf-8">
<title>Kestrel Sound — Business Cards</title>
<link href="https://fonts.googleapis.com/css2?family=Barlow:wght@400;500;600;700&display=swap" rel="stylesheet">
<style>
  :root {
    --backdrop: #dbd7d7;
    --blue: #0a69ad;
    --cyan: #00b7e3;
    --white: #ffffff;
    --pale-stripe: #c9d7ef;
    --sky-stripe: #63c8ef;
    --mid-stripe: #3f8fcb;
    --grey-text: #7d8a96;
  }
  * { margin: 0; padding: 0; box-sizing: border-box; }
  html, body {
    width: 1200px; height: 900px; overflow: hidden;
    background: var(--backdrop);
    font-family: "Barlow", Arial, sans-serif;
  }
  .sheet { position: relative; width: 1200px; height: 900px; }

  .card {
    position: absolute; width: 366px; height: 202px;
    border-radius: 12px; overflow: hidden;
    box-shadow: 0 3px 8px rgba(0,0,0,0.28);
  }
  .card--white { background: var(--white); }
  .card--blue { background: var(--blue); }
  .card--cyan { background: var(--cyan); }

  .card--a { left: 53px; top: 56px; }
  .card--b { left: 467px; top: 56px; }
  .card--c { left: 357px; top: 338px; }
  .card--d { left: 771px; top: 338px; }
  .card--e { left: 53px; top: 632px; }
  .card--f { left: 466px; top: 632px; }

  /* Front */
  .tab { position: absolute; top: 89px; width: 26px; height: 26px; }
  .tab--left { left: 0; }
  .tab--right { right: 0; }
  .tab--cyan { background: var(--cyan); }
  .tab--blue { background: var(--blue); }
  .tab--white { background: var(--white); }

  .brand {
    font-weight: 700; letter-spacing: -0.2px; white-space: nowrap;
  }
  .brand--front {
    position: absolute; left: 0; right: 0; top: 80px;
    text-align: center; font-size: 32px; line-height: 40px;
  }
  .brand--blue { color: var(--blue); }
  .brand--white { color: var(--white); }

  /* Back */
  .brand--back { position: absolute; font-size: 18px; line-height: 20px; }

  .stripes {
    position: absolute; top: 89px; height: 26px; width: 152px;
    display: flex; justify-content: space-between;
  }
  .stripes span { display: block; width: 7px; height: 100%; }
  .stripes--white-sky span { background: var(--white); }
  .stripes--white-sky span:nth-child(n+6) { background: var(--sky-stripe); }
  .stripes--blue-white span { background: var(--white); }
  .stripes--blue-white span:nth-child(-n+5) {
    background: linear-gradient(var(--mid-stripe) 50%, var(--blue) 50%);
  }
  .stripes--pale span { background: var(--pale-stripe); }

  .details { position: absolute; font-size: 10px; line-height: 12px; }
  .details--right { text-align: right; }
  .person__name { font-size: 12.5px; font-weight: 600; line-height: 15px; }
  .person__role { font-size: 11px; line-height: 13px; }
  .contact { margin-top: 26px; }
  .contact__web { margin-top: 14px; font-weight: 600; }

  .details--on-blue .person__name { color: var(--cyan); }
  .details--on-blue { color: var(--white); }
  .details--on-cyan .person__name, .details--on-cyan .person__role { color: var(--blue); }
  .details--on-cyan .contact { color: var(--white); }
  .details--on-cyan .contact__web { color: var(--blue); }
  .details--on-white .person__name { color: var(--blue); }
  .details--on-white .person__role, .details--on-white .contact { color: var(--grey-text); }
  .details--on-white .contact__web { color: var(--blue); }
</style>
</head>
<body>
<main class="sheet">

  <!-- Card set 1: white front -->
  <section class="card card--white card--a">
    <div class="tab tab--left tab--cyan"></div>
    <div class="tab tab--right tab--blue"></div>
    <p class="brand brand--front brand--blue">Kestrel Sound</p>
  </section>

  <section class="card card--blue card--b">
    <p class="brand brand--back brand--white" style="left:27px; top:30px;">Kestrel Sound</p>
    <div class="stripes stripes--white-sky" style="left:0;">
      <span></span><span></span><span></span><span></span><span></span><span></span><span></span><span></span><span></span><span></span>
    </div>
    <div class="details details--on-blue" style="left:165px; top:86px;">
      <p class="person__name">Bartholomew Quenneville</p>
      <p class="person__role">Audio Engineer</p>
      <div class="contact">
        <p>Phone: 0478 615 027</p>
        <p>bartholomew@kestrelsound.com.au</p>
        <p class="contact__web">www.kestrelsound.com.au</p>
      </div>
    </div>
  </section>

  <!-- Card set 2: cyan back -->
  <section class="card card--cyan card--c">
    <p class="brand brand--back brand--blue" style="right:167px; top:30px;">Kestrel Sound</p>
    <div class="details details--right details--on-cyan" style="right:167px; top:86px;">
      <p class="person__name">Bartholomew Quenneville</p>
      <p class="person__role">Audio Engineer</p>
      <div class="contact">
        <p>Phone: 0478 615 027</p>
        <p>bartholomew@kestrelsound.com.au</p>
        <p class="contact__web">www.kestrelsound.com.au</p>
      </div>
    </div>
    <div class="stripes stripes--blue-white" style="right:0; width:151px;">
      <span></span><span></span><span></span><span></span><span></span><span></span><span></span><span></span><span></span><span></span>
    </div>
  </section>

  <section class="card card--white card--d">
    <div class="tab tab--left tab--cyan"></div>
    <div class="tab tab--right tab--blue"></div>
    <p class="brand brand--front brand--blue">Kestrel Sound</p>
  </section>

  <!-- Card set 3: blue front, white back -->
  <section class="card card--blue card--e">
    <div class="tab tab--left tab--cyan"></div>
    <div class="tab tab--right tab--white"></div>
    <p class="brand brand--front brand--white">Kestrel Sound</p>
  </section>

  <section class="card card--white card--f">
    <p class="brand brand--back brand--blue" style="left:30px; top:48px;">Kestrel Sound</p>
    <div class="stripes stripes--pale" style="left:0; width:151px;">
      <span></span><span></span><span></span><span></span><span></span><span></span><span></span><span></span><span></span><span></span>
    </div>
    <div class="details details--on-white" style="left:168px; top:86px;">
      <p class="person__name">Bartholomew Quenneville</p>
      <p class="person__role">Audio Engineer</p>
      <div class="contact">
        <p>Phone: 0478 615 027</p>
        <p>bartholomew@kestrelsound.com.au</p>
        <p class="contact__web">www.kestrelsound.com.au</p>
      </div>
    </div>
  </section>

</main>
</body>
</html>
```